Landing-Page-Design für Immobilienunternehmen
Zielgruppe
Die Firma Halvak Immobilien kauft jegliche Art von Immobilien im Osten von Hamburg. Die Zielgruppe sind Immobilienbesitzer, welche ihre Wohnung, Haus, Gewerbe oder Sonstiges verkaufen möchten/müssen.
Ich würde gerne drei Unterzielgruppe mehr ansprechen:
Verkauf weil geerbt
textlich untermauert
Verkauf weil ins Altersheim
Verkauf weil ein Geldengpass
Wir kaufen:
Häuser
Eigentumswohnungen
Gewerbeflächen
Mehrfamilienhäuser
Garagen
Agrarflächen (Wald, Acker, Wiese, Teiche)
Aufgabenstellung
Es besteht ein Logo, welches berücksichtigt werden müsste.
Außerdem:
- responsive
- seriös
- conversion optimiert
- viel bebildert, textliche untermauert
- vertrauensvoll/verschwiegen
Telefonnummer soll prominent dargestellt werden, genauso wie ein Kontaktformular.

```html
<!DOCTYPE html>
<html lang="de">
<head>
<meta charset="utf-8">
<title>Halvak Immobilien – Wir kaufen Immobilien</title>
<link rel="stylesheet" href="https://fonts.googleapis.com/css2?family=Roboto+Condensed:wght@300;400;700&family=Arimo:wght@400&family=Roboto:ital,wght@0,700;1,700&display=swap">
<style>
  :root {
    --green: #79b82a;
    --ink: #2f3a44;
    --text: #6d6d6d;
    --panel: #f2f2f2;
    --white: #ffffff;
  }
  * { box-sizing: border-box; margin: 0; padding: 0; }
  html, body { width: 1200px; height: 977px; overflow: hidden; }
  body { background: var(--white); font-family: "Arimo", Arial, sans-serif; position: relative; }

  .brand { position: absolute; left: 130px; top: 86px; display: flex; align-items: center; gap: 18px; }
  .brand-mark { width: 26px; height: 26px; background: var(--green); }
  .brand-name { font-family: "Roboto Condensed", sans-serif; font-weight: 700; font-size: 54px; color: var(--ink); letter-spacing: 1px; line-height: 1; }
  .brand-tagline { position: absolute; left: 174px; top: 154px; font-family: "Roboto Condensed", sans-serif; font-size: 19px; letter-spacing: 2px; color: var(--ink); }

  .claim { position: absolute; right: 30px; top: 10px; width: 470px; height: 190px; }
  .claim-text { position: absolute; left: 40px; top: 26px; width: 420px; transform: rotate(-6deg); color: var(--white); font-family: "Roboto", sans-serif; font-weight: 700; font-size: 30px; line-height: 1.12; text-align: center; }

  .intro { position: absolute; top: 272px; left: 0; width: 100%; text-align: center; }
  .intro h1 { font-family: "Roboto Condensed", sans-serif; font-weight: 300; font-size: 34px; color: var(--green); }
  .intro p { font-family: "Roboto Condensed", sans-serif; font-size: 20px; color: var(--text); margin-top: 4px; }

  .cards { position: absolute; top: 370px; left: 150px; display: flex; gap: 35px; align-items: flex-start; }
  .card { width: 300px; }
  .card:nth-child(3) { margin-top: -12px; }
  .card-title { height: 42px; background: var(--green); color: var(--white); font-family: "Roboto Condensed", sans-serif; font-weight: 400; font-size: 20px; letter-spacing: 1px; display: flex; align-items: center; justify-content: center; }
  .card-photo { height: 190px; }
  .photo-hands { background: linear-gradient(160deg, #d9dbdc, #b9bcbd); }
  .photo-face { background: linear-gradient(120deg, #f3f1ef, #c9b8ab); }
  .photo-window { background: linear-gradient(100deg, #e9eaec, #8d9296); }
  .card-body { background: var(--panel); padding: 16px 30px 18px; height: 230px; font-size: 17px; line-height: 25px; color: var(--text); text-align: justify; hyphens: auto; }
  .card:nth-child(3) .card-body { height: 248px; padding-top: 22px; }
  .card-more { color: var(--green); float: right; }

  .call { position: absolute; top: 838px; left: 290px; display: flex; align-items: center; gap: 28px; }
  .call-label { width: 130px; height: 68px; background: var(--green); color: var(--white); font-family: "Roboto", sans-serif; font-weight: 700; font-size: 18px; line-height: 1.15; display: flex; align-items: center; justify-content: center; text-align: center; transform: rotate(-3deg); }
  .call-number { font-family: "Roboto", sans-serif; font-weight: 700; font-style: italic; font-size: 38px; color: var(--green); letter-spacing: 1px; margin-top: 10px; }
</style>
</head>
<body>
  <header>
    <div class="brand">
      <span class="brand-mark"></span>
      <span class="brand-name">HALVAK IMMOBILIEN</span>
    </div>
    <div class="brand-tagline">VERWALTUNG · BERATUNG · INVESTMENT</div>

    <div class="claim">
      <svg width="470" height="190" viewBox="0 0 470 190" aria-hidden="true">
        <polygon points="10,40 465,0 470,135 130,160 95,190 85,162 20,168" fill="var(--green)"/>
      </svg>
      <p class="claim-text">Wir kaufen Immobilien<br>jeglicher Art<br>im Osten von Hamburg!</p>
    </div>
  </header>

  <section class="intro">
    <h1>BEI UNS IST IHRE IMMOBILIE IN GUTER HAND</h1>
    <p>Egal, warum Sie verkaufen wollen!</p>
  </section>

  <section class="cards">
    <article class="card">
      <h2 class="card-title">SIE HABEN GEERBT?</h2>
      <div class="card-photo photo-hands" role="img" aria-label="Foto: ältere Hände halten ein kleines Holzhaus"></div>
      <p class="card-body">At vero eos et accusam et justo duo dolores et ea rebum. Stet clita kasd gubergren, no sea takimata sanctus est Lorem ipsum dolor sit amet. Lorem ipsum dolor sit amet, consetetur sadipscing elitr, sed diam nonu <span class="card-more">MEHR</span></p>
    </article>
    <article class="card">
      <h2 class="card-title">SIE GEHEN INS ALTERSHEIM?</h2>
      <div class="card-photo photo-face" role="img" aria-label="Foto: Seniorin in Nahaufnahme"></div>
      <p class="card-body">At vero eos et accusam et justo duo dolores et ea rebum. Stet clita kasd gubergren, no sea takimata sanctus est Lorem ipsum dolor sit amet. Lorem ipsum dolor sit amet, consetetur sadipscing elitr, sed diam nonu <span class="card-more">MEHR</span></p>
    </article>
    <article class="card">
      <h2 class="card-title">SIE HABEN GELDENGPASS?</h2>
      <div class="card-photo photo-window" role="img" aria-label="Foto: nachdenkliche Seniorin am Fenster"></div>
      <p class="card-body">At vero eos et accusam et justo duo dolores et ea rebum. Stet clita kasd gubergren, no sea takimata sanctus est Lorem ipsum dolor sit amet. Lorem ipsum dolor sit amet, consetetur sadipscing elitr, sed diam nonu <span class="card-more">MEHR</span></p>
    </article>
  </section>

  <section class="call">
    <div class="call-label">Rufen Sie<br>uns an!</div>
    <a class="call-number">+49 40 66969 123</a>
  </section>
</body>
</html>
```